Packaging design for health, nutrition, essential oils, herbals, vitamins and product lines. We want an upscale design that is aligned with nature. Must add a tree graphic into the design because our products are forest or tree products.

We need boxes, bottles, tags, labels for herbs, herbal formulas, vitamin bottles,

This is the text that will be on the packaging.

Larchmont Verdant Remedies (bold this)
-- insert eclectic tree graphic ---
Aligned With Nature
Est. Aspen, Colorado

The colors of our brand are
Platinum, White, Silver, Chrome, Clear Glass
The Graphic we need is an eclectic or cool forest tree preferably pine trees or christmas trees but we are also open to an eclectic tree graphic

We also need to see a tree graphic in the branding packaging
We are opened to adding some green to the packaging as well

Our products that we need the packaging for are
Herbs and Herbal Formulas
Beverages
Fragrances
Aromatherapy
Essential Oils
Nutritional Products
Vitamins, Supplements and Minerals

It is very important to provide us with a luxury brand that compliments our firm, Halcyon Clinicians.
This is a new division of our firm that delivers all
100% ALL NATURAL PLANT BASED PRODUCTS and INDIGENOUS MEDICINES

I love the idea of having
platinum or shiny silver contrast against minimalist white and or glass and a must have is to add green (forest or herbal green color) and a tree graphic

Again : Our products are all forest and plant based

We also will have the same designer create a web page for the commerce store after this project

Target Market(s)

Luxury Consumers, Plant Based Medicine and Natural Healing Consumers, Herbs and Herbal Formula Consumers, Health Conscious Consumers, Nature or Environmental Products Consumers, High Networth Consumers

Industry/Entity Type

Health Product

Requirements
Must have
• Colors : Platinum, Silver, Chrome, White and A Tree or Plant Leaves Graphic, Preferably a Forest Tree
• Maintain same font as our HalcyonClinicians.example logo brand
Should not have
• No other colors besides white, platinum, silver, chrome or forest or tree green

```html
<!DOCTYPE html>
<html lang="en">
<head>
<meta charset="utf-8">
<title>Larchmont Verdant Remedies – Rosemary Essential Oil Label</title>
<link href="https://fonts.googleapis.com/css2?family=Cinzel:wght@400;600;700&display=swap" rel="stylesheet">
<style>
  :root {
    --canvas: #f1f1f1;
    --label-silver: #c3c3c3;
    --ink: #1b1b1b;
    --ink-soft: #3a3a3a;
    --heading: #4b4b4b;
    --forest-mist: #a7b2aa;
    --forest-mid: #6f7b72;
    --forest-deep: #0e0e0e;
    --foil-black: #000000;
    --foil-silver: #f4f4f4;
    --foil-shade: #bdbdbd;
  }
  * { box-sizing: border-box; margin: 0; padding: 0; }
  html, body {
    width: 1200px; height: 1200px; overflow: hidden;
    background: var(--canvas);
    font-family: "Cinzel", "Times New Roman", serif;
  }
  .sheet { position: relative; width: 1200px; height: 1200px; }

  .layer-title {
    position: absolute; top: 280px; width: 440px;
    text-align: center; font-weight: 700; font-size: 28px;
    letter-spacing: 2px; color: var(--heading);
  }
  .layer-title--print { left: 120px; }
  .layer-title--foil { left: 640px; }

  .label {
    position: absolute; top: 330px; width: 440px; height: 645px;
    overflow: hidden;
  }
  .label--print { left: 120px; background: var(--label-silver); }
  .label--foil { left: 640px; background: var(--foil-black); }

  .brand-mark {
    position: absolute; left: 207px; top: 30px;
    width: 26px; height: 26px; border: 2px solid var(--ink-soft);
    background: #e6e6e6;
  }
  .brand-name {
    position: absolute; top: 76px; width: 100%; text-align: center;
    font-weight: 700; font-size: 14px; letter-spacing: 1.6px; color: var(--ink);
  }
  .brand-origin {
    position: absolute; top: 97px; width: 100%; text-align: center;
    font-size: 9px; letter-spacing: 0.6px; color: var(--ink-soft);
  }
  .rule {
    position: absolute; left: 20px; width: 400px; height: 0;
    border-top: 3px dotted var(--ink-soft);
  }
  .rule--top { top: 175px; }
  .rule--bottom { top: 283px; }
  .label--foil .rule { border-top-color: var(--foil-silver); }

  .product-name {
    position: absolute; top: 188px; width: 100%; text-align: center;
    font-weight: 700; font-size: 36px; letter-spacing: 1px; color: var(--ink);
  }
  .product-type {
    position: absolute; top: 245px; width: 100%; text-align: center;
    font-weight: 700; font-size: 20px; letter-spacing: 1.5px; color: var(--ink);
  }

  .forest {
    position: absolute; left: 0; top: 320px; width: 440px; height: 325px;
    background: linear-gradient(180deg, var(--label-silver) 0%, var(--forest-mist) 22%, var(--forest-mid) 50%, var(--forest-deep) 80%, var(--forest-deep) 100%);
  }
  .foil-forest {
    position: absolute; left: 0; top: 400px; width: 440px; height: 180px;
    background: linear-gradient(180deg, var(--foil-black) 0%, var(--foil-shade) 25%, var(--foil-silver) 60%, var(--foil-black) 100%);
  }

  .tagline {
    position: absolute; top: 612px; width: 100%; text-align: center;
    font-weight: 600; font-size: 16px; letter-spacing: 2px;
    color: var(--foil-silver);
  }
</style>
</head>
<body>
<main class="sheet">
  <h2 class="layer-title layer-title--print">Printed Graphics</h2>
  <section class="label label--print">
    <div class="brand-mark" aria-hidden="true"></div>
    <p class="brand-name">LARCHMONT VERDANT REMEDIES</p>
    <p class="brand-origin">EST. ASPEN, COLORADO</p>
    <div class="rule rule--top"></div>
    <p class="product-name">100% ROSEMARY</p>
    <p class="product-type">ESSENTIAL OIL</p>
    <div class="rule rule--bottom"></div>
    <div class="forest" role="img" aria-label="Layered pine forest silhouette fading from misty sage green to black"></div>
    <p class="tagline">Aligned with Nature</p>
  </section>

  <h2 class="layer-title layer-title--foil">Silver Foiling</h2>
  <section class="label label--foil">
    <div class="rule rule--top"></div>
    <div class="rule rule--bottom"></div>
    <div class="foil-forest" role="img" aria-label="Silver foil pine tree silhouettes along the forest line"></div>
    <p class="tagline">Aligned with Nature</p>
  </section>
</main>
</body>
</html>
```